Web Design Project

I am looking for a simple website to promote my business called Wyllard Benick Consulting. We provide consulting and implementation services for finance and supply chain processes and systems.

We want to project a professional but innovative image. I have attached a copy of our logo. It is not necessary to stick with the colours in the logo - we encourage you to experiment with the colours and even to change the colours of the logo to fit with your design. Although, on the front page we would like to have the logo with its original colours.

Required sections:
About
What we do
Clients
Contact
Updates

Target Market(s)

Medium to large companies including multi-nationals in all industries.

Industry/Entity Type

Finance

Requirements
Must have
• Required sections:
About
What we do
Clients
Contact

```html
<!DOCTYPE html>
<html lang="en">
<head>
<meta charset="utf-8">
<title>Wyllard Benick Consulting</title>
<link href="https://fonts.googleapis.com/css2?family=Source+Sans+3:wght@300;400;600&display=swap" rel="stylesheet">
<style>
:root{
  --page:#e8e8e8;
  --white:#ffffff;
  --ink:#555555;
  --ink-soft:#777777;
  --ink-muted:#8a8a8a;
  --brand-blue:#1f5fa8;
  --lime:#b5cc2e;
  --lime-deep:#9db124;
  --lime-line:#c9d86a;
  --rule:#e2e2e2;
  --quote-bg:#dcdcd3;
  --photo-a:#f3f4f5;
  --photo-b:#d9dde0;
}
*{box-sizing:border-box;margin:0;padding:0}
html,body{width:1200px;height:874px;overflow:hidden}
body{background:var(--page);font-family:"Source Sans 3",sans-serif;color:var(--ink);position:relative}
.site{position:absolute;left:197px;top:0;width:806px}

/* header */
.header{position:absolute;left:0;top:0;width:806px;height:375px;background:linear-gradient(90deg,#ffffff 0%,#f7f8f8 40%,#eceeef 100%)}
.hero-photo{position:absolute;right:0;top:0;width:300px;height:375px;background:linear-gradient(180deg,var(--photo-a),var(--photo-b) 35%,#3a3d42 70%,#2b2d31 100%)}
.sidebar{position:absolute;left:0;top:0;width:257px;height:375px;background:var(--white);box-shadow:inset 0 0 40px rgba(0,0,0,.06),2px 0 6px rgba(0,0,0,.05)}
.brand{position:absolute;left:52px;top:54px;width:156px;text-align:center;color:var(--brand-blue);font-weight:400}
.brand-dot{display:block;width:58px;height:58px;border-radius:50%;background:var(--lime);margin:0 auto 14px}
.brand-name{display:block;font-size:17px;letter-spacing:.5px;line-height:1}
.brand-sub{display:block;font-size:12.5px;letter-spacing:.8px;margin-top:3px}
.nav{position:absolute;left:52px;top:183px;width:154px;list-style:none}
.nav li{height:34.3px;border-bottom:1px solid var(--rule);font-size:11.5px;color:var(--ink-muted);padding-top:4px}
.nav li:first-child{border-bottom-color:var(--lime-line);color:var(--ink-soft)}
.nav li:last-child{border-bottom:none}
.hero-text{position:absolute;left:311px;top:129px;width:260px}
.hero-title{font-size:31px;font-weight:600;line-height:31px;color:var(--ink)}
.hero-lead{font-size:11.5px;line-height:20.5px;margin-top:12px;color:var(--ink)}

/* services */
.services{position:absolute;left:0;top:375px;width:1200px;height:180px;background:var(--lime-deep)}
.services-inner{position:absolute;left:197px;top:0;width:806px;height:180px;background:var(--lime)}
.service{position:absolute;top:33px;width:215px;color:var(--white)}
.service h2{font-size:20.5px;font-weight:600;line-height:26px}
.service p{font-size:11.5px;line-height:20.5px;margin-top:6px}

/* testimonial */
.testimonial{position:absolute;left:0;top:555px;width:806px;height:223px;background:var(--quote-bg);box-shadow:0 12px 14px -8px rgba(0,0,0,.18)}
.client-photo{position:absolute;left:52px;top:30px;width:110px;height:110px;border:4px solid var(--white);background:linear-gradient(180deg,#a49d90,#7f8890 60%,#5b7fb8)}
.quote-mark{position:absolute;left:194px;top:20px;font-size:50px;font-weight:600;color:var(--ink);line-height:1}
.quote-text{position:absolute;left:234px;top:56px;width:530px;font-size:20.5px;font-weight:300;line-height:26px;color:var(--ink)}
.quote-by{position:absolute;right:53px;top:167px;font-size:14px;color:var(--ink)}
.quote-by strong{font-weight:600}
.quote-by span{color:var(--lime-deep);font-weight:300}

/* footer */
.footer{position:absolute;left:0;top:815px;width:806px;height:20px;font-size:11px;color:var(--ink-soft)}
.footer .copy{position:absolute;left:7px;top:1px}
.contact{position:absolute;top:1px;display:flex;align-items:center;gap:8px}
.social{position:absolute;left:718px;top:1px;display:flex;gap:14px}
.social i{display:block;width:14px;height:14px;background:#8a8a8a;border-radius:2px}
</style>
</head>
<body>
<div class="site">
  <header class="header">
    <div class="hero-photo" role="img" aria-label="Portrait photo of a smiling businessman in a dark suit, arms crossed, bright office background"></div>
    <aside class="sidebar">
      <div class="brand">
        <span class="brand-dot"></span>
        <span class="brand-name">WYLLARD BENICK</span>
        <span class="brand-sub">CONSULTING LIMITED</span>
      </div>
      <ul class="nav">
        <li>Home</li>
        <li>About</li>
        <li>What We Do</li>
        <li>Clients</li>
        <li>Contact</li>
      </ul>
    </aside>
    <div class="hero-text">
      <h1 class="hero-title">We Professional<br>&amp; Inovative</h1>
      <p class="hero-lead">Duis autem vel eum iriure dolor in hendrerit<br>in vulputate velit esse molestie</p>
    </div>
  </header>
</div>

<section class="services">
  <div class="services-inner">
    <div class="service" style="left:52px">
      <h2>Finance</h2>
      <p>Duis autem vel eum iriure dolor in hendrerit in vulputate velit esse molestie consequat, vel illum dolore eu feugiat nulla facilisis at vero.</p>
    </div>
    <div class="service" style="left:301px">
      <h2>Supply Chain</h2>
      <p>Duis autem vel eum iriure dolor in hendrerit in vulputate velit esse molestie consequat, vel illum dolore eu feugiat nulla facilisis at vero.</p>
    </div>
    <div class="service" style="left:549px">
      <h2>System</h2>
      <p>Duis autem vel eum iriure dolor in hendrerit in vulputate velit esse molestie consequat, vel illum dolore eu feugiat nulla facilisis at vero.</p>
    </div>
  </div>
</section>

<div class="site">
  <section class="testimonial">
    <div class="client-photo" role="img" aria-label="Photo of a smiling client wearing a black hat and blue shirt"></div>
    <div class="quote-mark">&ldquo;</div>
    <p class="quote-text">Truly professional and reliable consultancy agency, able to give me the best solution for the financial, thankyou.</p>
    <p class="quote-by"><strong>Dario</strong>, <span>Enterpreneur</span></p>
  </section>

  <footer class="footer">
    <span class="copy">Copyright &copy; 2013 Wyllard Benick Consulting. All right reserved</span>
    <span class="contact" style="left:358px">
      <svg width="12" height="14" viewBox="0 0 12 14"><path d="M3 1 L5 4 L3.6 5.6 C4.4 7.6 5.6 9 7.4 10 L9 8.6 L11.5 10.8 L10 13 C5 12.5 1 8 1 2.5 Z" fill="#999"/></svg>
      +768 555 0142
    </span>
    <span class="contact" style="left:468px">
      <svg width="16" height="11" viewBox="0 0 16 11"><rect x="0" y="0" width="16" height="11" fill="#999"/><path d="M0 0 L8 6 L16 0" stroke="#e8e8e8" stroke-width="1.3" fill="none"/></svg>
      <span style="margin-left:10px">info@wyllard-benick-consulting.com</span>
    </span>
    <div class="social" aria-label="Social links"><i></i><i></i><i></i></div>
  </footer>
</div>
</body>
</html>
```